New Optometry Practice needs a Business Card

Need a business card for an Optometry practice called 'Marlow Vista Eyecare'. I would like to use designs that are friendly, fun and professional. Looking to incorporate glasses (see uploaded image). Not interested in design with an 'eye' in logo. Like green, blue, white as color choices..but open to your ideas. Back of card will be an appointment card as well as provide address, phone and email information.

Industry/Entity Type

Business

Contact Information for Business Card

Marlow Vista Eyecare
Dr. Petra Lindqvist, Optometrist (or O.D.)
4172 S Corbell Ave Wenatchee, WA 98736
PMarlowvistaeyecare.example

Colors
acd036
33b8a4
f68d4e
cfeae6
fee18a
cadf82

Requirements
Must have
• Appointment card on back with date/time of return for next exam

```html
<!DOCTYPE html>
<html lang="en">
<head>
<meta charset="utf-8">
<title>Marlow Vista Eyecare – Business Card</title>
<link rel="stylesheet" href="https://fonts.googleapis.com/css2?family=Arimo:wght@400&family=Tinos:wght@700&display=swap">
<style>
  :root {
    --teal: #17aa94;
    --ink: #000000;
    --paper: #ffffff;
    --backdrop: #e9e6e1;
    --text-dark: #1a1a1a;
    --rule: #9a9a9a;
  }
  html, body {
    margin: 0;
    width: 1200px;
    height: 933px;
    overflow: hidden;
    background: var(--backdrop);
  }
  .canvas {
    position: relative;
    width: 1200px;
    height: 933px;
  }
  .card {
    position: absolute;
    left: 274px;
    width: 652px;
    height: 374px;
    box-shadow: 0 4px 14px rgba(0,0,0,0.25);
  }
  .card--front { top: 64px; }
  .card--back { top: 494px; }
  .card svg { display: block; width: 100%; height: 100%; }
  .brand-name {
    font-family: "Tinos", "Times New Roman", serif;
    font-weight: 700;
    font-size: 52px;
    fill: var(--text-dark);
  }
  .doctor-name {
    font-family: "Arimo", Arial, sans-serif;
    font-size: 38px;
    fill: var(--teal);
    word-spacing: 4px;
  }
  .doctor-title {
    font-family: "Arimo", Arial, sans-serif;
    font-size: 24px;
    fill: var(--text-dark);
    word-spacing: 3px;
  }
  .appointment-label {
    font-family: "Arimo", Arial, sans-serif;
    font-size: 19px;
    fill: var(--teal);
  }
  .appointment-field {
    font-family: "Arimo", Arial, sans-serif;
    font-size: 18px;
    fill: var(--text-dark);
  }
  .appointment-rule { stroke: var(--rule); stroke-width: 1.2; }
  .contact-line {
    font-family: "Arimo", Arial, sans-serif;
    font-size: 22px;
    fill: var(--paper);
    word-spacing: 5px;
  }
  .fill-teal { fill: var(--teal); }
  .fill-ink { fill: var(--ink); }
  .fill-paper { fill: var(--paper); }
  .edge-line { fill: none; stroke: var(--paper); stroke-width: 3; }
</style>
</head>
<body>
<main class="canvas">

  <section class="card card--front" aria-label="Card front">
    <svg viewBox="0 0 816 467" preserveAspectRatio="none">
      <rect class="fill-teal" width="816" height="467"/>
      <path class="fill-ink" d="M95,467 C200,250 450,40 790,0 L816,0 L816,467 Z"/>
      <path class="edge-line" d="M93,467 C198,250 448,38 790,-2"/>
      <path class="fill-paper" d="M200,467 C180,320 420,50 816,0 L816,467 Z"/>
      <text class="brand-name" x="776" y="395" text-anchor="end">Marlow Vista Eyecare</text>
    </svg>
  </section>

  <section class="card card--back" aria-label="Card back">
    <svg viewBox="0 0 816 467" preserveAspectRatio="none">
      <rect class="fill-teal" width="816" height="467"/>
      <path class="fill-ink" d="M616,0 L718,0 C600,250 300,430 80,467 L0,467 C500,330 640,150 616,0 Z"/>
      <path class="edge-line" d="M720,-1 C602,251 302,431 82,469"/>
      <path class="fill-paper" d="M0,0 L616,0 C640,150 500,330 0,467 Z"/>

      <text class="brand-name" x="45" y="104">Marlow Vista Eyecare</text>
      <text class="doctor-name" x="40" y="205">Dr. Petra Lindqvist</text>
      <text class="doctor-title" x="41" y="243">Optometrist (or O.D.)</text>

      <g class="appointment">
        <text class="appointment-label" x="41" y="296">Your next exam</text>
        <text class="appointment-field" x="41" y="330">Date</text>
        <line class="appointment-rule" x1="86" y1="332" x2="196" y2="332"/>
        <text class="appointment-field" x="210" y="330">Time</text>
        <line class="appointment-rule" x1="256" y1="332" x2="340" y2="332"/>
      </g>

      <text class="contact-line" x="755" y="365" text-anchor="end">PMarlowvistaeyecare.example</text>
      <text class="contact-line" x="755" y="403" text-anchor="end">4172 S Corbell Ave Wenatchee</text>
      <text class="contact-line" x="755" y="441" text-anchor="end">WA 98736</text>

      <g class="icon-web" transform="translate(770,350)">
        <rect class="fill-paper" width="18" height="18"/>
        <circle cx="9" cy="9" r="6" fill="none" stroke="var(--teal)" stroke-width="1.6"/>
        <path d="M3,9 H15 M9,3 C5,7 5,11 9,15 M9,3 C13,7 13,11 9,15" fill="none" stroke="var(--teal)" stroke-width="1.2"/>
      </g>
      <g class="icon-pin" transform="translate(770,388)">
        <rect class="fill-paper" width="18" height="18"/>
        <path class="fill-teal" d="M9,3 C6,3 5,5 5,7 C5,10 9,15 9,15 C9,15 13,10 13,7 C13,5 12,3 9,3 Z"/>
        <circle class="fill-paper" cx="9" cy="7" r="1.6"/>
      </g>
    </svg>
  </section>

</main>
</body>
</html>
```